Elk R Cellars Wine Label Design

We are looking to redesign our wine labels. i have updated this contest to focus on just the premium wines. These should have gold writing on a silk screened bottle, or on black traditional label. Red or gold capsule.
Our logo is of a mountain with dated cursive script (see attached). We are hoping to maintain some of that brand identity but with a more premium look. The current cursive script definitely needs to be altered. Elk Ridge is an extinct volcano that is a local landmark in the Okanagan Valley. One concept was using this image as a background or element of the labels or a new logo. i have attached an actual photo of the mountain. This is only to inspire a simplified logo.

Target Market(s)

30-65

Logo Text

Elk. (or Elk) Ravensworth

Font styles to use
Serif
Script

Colors
1b1b1b
ec1f27
fbf289

Requirements
Must have
• High End Feel. silkscreen? gold writing. wine is called "Lantern"
Nice to have
• "estate grown"

```html
<!DOCTYPE html>
<html lang="en">
<head>
<meta charset="utf-8">
<title>Elk R Cellars – Lantern Label Concepts</title>
<link href="https://fonts.googleapis.com/css2?family=Cinzel:wght@400;500&family=Cormorant+SC:wght@500&family=Pinyon+Script&family=Open+Sans:wght@400&display=swap" rel="stylesheet">
<style>
  :root {
    --page: #ffffff;
    --print-ground: #1b1b1b;
    --gold: #d9a441;
    --gold-deep: #b8812c;
    --silver: #c9c9c9;
    --caption: #b3b3b3;
  }
  * { margin: 0; padding: 0; box-sizing: border-box; }
  html, body { width: 1200px; height: 1000px; overflow: hidden; background: var(--page); }
  .canvas { position: relative; width: 1200px; height: 1000px; }

  .variant { position: absolute; top: 0; width: 230px; height: 1000px; }
  .variant--a { left: 38px; }
  .variant--b { left: 338px; }
  .variant--c { left: 635px; }
  .variant--d { left: 930px; }

  .variant-caption {
    position: absolute; top: 14px; width: 100%; text-align: center;
    font-family: "Open Sans", sans-serif; font-size: 24px; color: var(--caption);
  }

  .print-area {
    position: absolute; left: 12px; top: 80px; width: 206px; height: 835px;
    background: var(--print-ground); border-radius: 16px;
  }

  .brand-mark {
    position: absolute; left: 0; top: 362px; width: 100%;
    display: flex; align-items: center; justify-content: center; gap: 8px;
    font-family: "Cinzel", serif; font-size: 12px; letter-spacing: 2px; color: var(--gold);
  }
  .brand-mark .brand-dot { width: 18px; height: 18px; border-radius: 50%; background: var(--gold); }
  .finish-silver .brand-mark { color: var(--silver); }
  .finish-silver .brand-mark .brand-dot { background: var(--silver); }

  .estate-line {
    position: absolute; left: 0; top: 424px; width: 100%; text-align: center;
    font-family: "Cinzel", serif; font-size: 12.5px; letter-spacing: 2.4px; color: var(--gold-deep);
  }
  .estate-line--script {
    font-family: "Pinyon Script", cursive; font-size: 15px; letter-spacing: 0; top: 420px; color: var(--gold);
  }

  .wine-name {
    position: absolute; left: 0; top: 438px; width: 100%; text-align: center;
    font-family: "Cinzel", serif; font-weight: 500; font-size: 31px; letter-spacing: 1px; color: var(--gold-deep);
  }

  .region {
    position: absolute; left: 0; top: 662px; width: 100%; text-align: center;
    font-family: "Cormorant SC", serif; font-size: 15px; letter-spacing: 1.2px; color: var(--gold-deep);
  }
  .region--script {
    font-family: "Pinyon Script", cursive; font-size: 20px; letter-spacing: 0; top: 656px; color: var(--gold);
  }

  .vintage {
    position: absolute; left: 0; top: 683px; width: 100%; text-align: center;
    font-family: "Cinzel", serif; font-size: 27px; color: var(--gold);
  }
</style>
</head>
<body>
<main class="canvas">

  <section class="variant variant--a finish-gold">
    <p class="variant-caption">v4a</p>
    <div class="print-area">
      <div class="brand-mark"><span class="brand-dot"></span><span>ELK R CELLARS</span></div>
      <p class="estate-line">ESTATE GROWN</p>
      <h2 class="wine-name">LANTERN</h2>
      <p class="region">Okanagan Valley</p>
      <p class="vintage">2016</p>
    </div>
  </section>

  <section class="variant variant--b finish-silver">
    <p class="variant-caption">v4b</p>
    <div class="print-area">
      <div class="brand-mark"><span class="brand-dot"></span><span>ELK R CELLARS</span></div>
      <p class="estate-line">ESTATE GROWN</p>
      <h2 class="wine-name">LANTERN</h2>
      <p class="region">Okanagan Valley</p>
      <p class="vintage">2016</p>
    </div>
  </section>

  <section class="variant variant--c finish-gold">
    <p class="variant-caption">v4c</p>
    <div class="print-area">
      <div class="brand-mark"><span class="brand-dot"></span><span>ELK R CELLARS</span></div>
      <p class="estate-line estate-line--script">Estate Grown</p>
      <h2 class="wine-name">LANTERN</h2>
      <p class="region region--script">Okanagan Valley</p>
      <p class="vintage">2016</p>
    </div>
  </section>

  <section class="variant variant--d finish-silver">
    <p class="variant-caption">v4d</p>
    <div class="print-area">
      <div class="brand-mark"><span class="brand-dot"></span><span>ELK R CELLARS</span></div>
      <p class="estate-line estate-line--script">Estate Grown</p>
      <h2 class="wine-name">LANTERN</h2>
      <p class="region region--script">Okanagan Valley</p>
      <p class="vintage">2016</p>
    </div>
  </section>

</main>
</body>
</html>
```